Velmora Diagnostics Website

Project Description – Velmora Website Design
We need a clean, modern, and professional website for Velmora Diagnostics, a Ashgrove Hollis University of Dunmere spin-out focused on early cancer detection. Our first product, GlandSURE™, is a urine-based risk assessment test for pancreatic cancer, supported by strong clinical validation and partnerships with leading hospitals.

The site should:

Communicate trust, innovation, and clinical credibility.
Feature a clear value proposition on the home page with strong calls to action for investors, clinicians, and partners.
Showcase our technology, science, and clinical evidence in a way that is accessible but authoritative.
Highlight our university heritage, team, and collaborators.
Include sections for products/services, news/press, and contact forms.
Be fully responsive, WordPress compatible, SEO-friendly, and WCAG 2.1 AA accessible.

We want a minimalist, elegant design with subtle animations, strong visuals (e.g., science/biotech imagery), and a clear structure for future growth.
Deliverables should include editable design files (Figma/Sketch/Adobe XD) and a style guide.

```html
<!DOCTYPE html>
<html lang="en">
<head>
<meta charset="utf-8">
<title>Velmora Diagnostics</title>
<link rel="stylesheet" href="https://fonts.googleapis.com/css2?family=Montserrat:wght@600;700;800&family=Poppins:wght@400;500;600&display=swap">
<style>
:root{
  --blue:#3a80d6;
  --blue-dark:#1f3f8c;
  --navy:#0b1838;
  --yellow:#f6c640;
  --sky:#7fd0f0;
  --text:#2b2b33;
  --muted:#666a75;
  --white:#ffffff;
}
*{box-sizing:border-box;margin:0;padding:0}
html,body{width:1200px;height:5204px;overflow:hidden;background:var(--white)}
body{font-family:"Poppins",sans-serif;color:var(--text);position:relative}
.abs{position:absolute}
h1,h2,h3{font-family:"Montserrat",sans-serif}
svg{display:block}
.brand{display:flex;align-items:center;gap:14px;font-family:"Poppins",sans-serif;font-weight:600;letter-spacing:2px;color:var(--blue)}
.brand-dot{width:44px;height:44px;border-radius:50%;background:var(--blue)}
/* header */
.site-header{top:0;left:0;width:1200px;height:120px;background:var(--white)}
.site-header .brand{position:absolute;left:70px;top:40px;font-size:26px}
.main-nav{position:absolute;right:78px;top:46px;display:flex;gap:58px;align-items:center;font-size:15px}
.main-nav a{color:var(--text);text-decoration:none}
.main-nav a.active{color:var(--blue);border-bottom:2px solid var(--yellow);padding-bottom:6px}
.main-nav a.pill{background:var(--blue);color:var(--white);padding:6px 20px;border-radius:18px}
/* hero */
.hero{top:120px;left:0;width:1200px;height:730px;background:linear-gradient(100deg,#c9d3dd 0%,#e9eef2 35%,#9fb3c0 65%,#5f8093 100%)}
.hero-fade{left:0;top:450px;width:1200px;height:280px;background:linear-gradient(180deg,rgba(255,255,255,0),rgba(255,255,255,.92) 60%)}
.play{left:575px;top:272px;width:52px;height:52px;border-radius:50%;background:var(--white)}
.hero h1{left:0;top:470px;width:1200px;text-align:center;font-size:62px;line-height:88px;font-weight:800;color:var(--blue-dark)}
.hero p{left:0;top:640px;width:1200px;text-align:center;font-size:26px;color:var(--navy)}
.btn-yellow{background:var(--yellow);color:var(--navy);font-weight:500;border-radius:30px;text-align:center}
.hero .btn-yellow{left:485px;top:708px;width:230px;height:58px;line-height:58px;font-size:22px}
/* features */
.features{top:919px;left:115px;width:970px;height:263px;background:var(--blue);border-radius:12px;box-shadow:0 6px 14px rgba(0,0,0,.15);display:flex;justify-content:space-around;padding:44px 40px 0}
.feature{width:200px;text-align:center;color:var(--white);font-size:19px;line-height:24px}
.feature-icon{width:106px;height:106px;margin:0 auto 18px;border-radius:50%;border:4px solid rgba(255,255,255,.7);display:flex;align-items:center;justify-content:center}
.feature-icon.y{background:var(--yellow)}
.feature-icon.b{background:var(--sky)}
/* about */
.about{top:1232px;left:0;width:1200px;height:646px;background:linear-gradient(180deg,#f5f6f9,#eceef3)}
.about-photo-a{left:115px;top:110px;width:218px;height:298px;border-radius:10px;background:linear-gradient(160deg,#dfe5ea,#7d93a8 60%,#2a3f66)}
.about-photo-b{left:340px;top:226px;width:220px;height:292px;border-radius:10px;background:linear-gradient(160deg,#3a4ed0,#9b3cc4 55%,#1a2a8a)}
.about-dot{left:305px;top:280px;width:74px;height:74px;border-radius:50%;background:var(--white);border:6px solid var(--sky)}
.about h2{left:616px;top:118px;font-size:52px;color:var(--blue);font-weight:600}
.rule{height:4px;width:46px;background:var(--yellow)}
.about .rule{left:618px;top:184px}
.about h3{left:616px;top:222px;font-family:"Poppins",sans-serif;font-weight:500;font-size:22px}
.about p{left:616px;top:272px;width:488px;font-size:13.5px;line-height:24px;color:var(--muted);text-align:justify}
.btn-blue{background:var(--blue);color:var(--white);border-radius:22px;text-align:center;font-size:14px}
.about .btn-blue{left:618px;top:471px;width:156px;height:38px;line-height:38px}
/* products */
.products{top:1878px;left:0;width:1200px;height:728px;background:radial-gradient(ellipse at 85% 40%,#274b8c 0%,#112556 40%,var(--navy) 80%)}
.products h2{left:0;top:48px;width:1200px;text-align:center;font-size:52px;color:var(--white);font-weight:600}
.products .rule{left:577px;top:130px}
.product-name{left:66px;top:188px;font-size:32px;font-weight:600;color:var(--yellow)}
.product-sub{left:66px;top:234px;font-size:15px;color:var(--white)}
.spec-list{left:66px;top:290px;width:640px;list-style:none}
.spec-list li{display:flex;gap:16px;align-items:flex-start;color:var(--white);font-size:15px;line-height:24px;margin-bottom:24px}
.spec-list li span.k{color:#6ea7f2}
.spec-icon{flex:0 0 40px;height:40px;border-radius:50%;background:var(--blue);border:2px solid #9cc4f5;margin-top:-6px;display:flex;align-items:center;justify-content:center}
.product-photo{left:798px;top:188px;width:343px;height:348px;border:3px solid var(--yellow);border-radius:14px;padding:10px}
.product-photo div{width:100%;height:100%;border-radius:8px;background:linear-gradient(135deg,#a8c4d8,#3a5875 50%,#c48a5a)}
/* tiles */
.tile{top:2515px;height:165px;width:338px;border-radius:8px;display:flex;align-items:center;gap:18px;padding:0 8px 0 28px;color:var(--white);font-size:23px;line-height:28px;font-weight:500}
.tile .t-icon{flex:0 0 86px;height:86px;border-radius:50%;background:var(--white);display:flex;align-items:center;justify-content:center}
.tile.blue{left:87px;background:var(--blue)}
.tile.sky{left:434px;background:var(--sky)}
.tile.yellow{left:780px;background:var(--yellow)}
/* info cards */
.card{top:2773px;width:325px;height:382px;background:var(--white);border-radius:10px;box-shadow:0 4px 16px rgba(0,0,0,.12);padding:10px}
.card .img{height:212px;border-radius:4px}
.card h4{font-weight:500;font-size:19px;color:var(--blue);margin:20px 18px 14px}
.card p{font-size:13px;line-height:20px;margin:0 18px;color:var(--text)}
.card .btn-yellow{display:block;width:130px;height:34px;line-height:34px;font-size:12px;color:var(--white);margin:28px auto 0}
/* blog */
.blog h2,.contact h2{width:1200px;left:0;text-align:center;font-size:52px;font-weight:600;color:var(--blue)}
.blog-card{top:3485px;width:320px;height:410px}
.blog-card .img{width:320px;height:270px}
.blog-card .body{position:absolute;left:44px;top:228px;width:276px;height:182px;background:var(--white);padding:14px 30px 0 30px}
.blog-card .date{font-size:10px;color:var(--yellow)}
.blog-card h4{font-size:15px;line-height:18px;color:var(--blue);font-weight:500;margin:6px 0 12px}
.blog-card p{font-size:12.5px;line-height:18px;color:var(--muted)}
.blog-card .btn-blue{display:inline-block;margin-top:10px;padding:3px 14px;font-size:10px;font-weight:600}
.arrow{top:3685px;width:36px;height:36px;border-radius:50%;background:var(--white);box-shadow:0 2px 8px rgba(0,0,0,.15)}
/* contact */
.contact-frame{left:69px;top:4157px;width:396px;height:414px;border:2px solid var(--yellow);border-radius:12px;padding:12px}
.contact-frame div{width:100%;height:100%;border-radius:6px;background:linear-gradient(160deg,#4a9fa6,#cfd8de 50%,#1f3b5e)}
.contact .rule{left:877px;top:4145px}
.field{background:var(--white);box-shadow:0 2px 10px rgba(0,0,0,.14);font-size:15px;color:#9a9ca4;padding:20px 24px}
.contact .btn-blue{left:553px;top:4557px;width:250px;height:52px;line-height:52px;font-size:16px;border-radius:28px}
.info{top:4712px;display:flex;align-items:center;gap:18px;font-size:15px;line-height:18px}
.info .ic{width:50px;height:50px;border-radius:50%;display:flex;align-items:center;justify-content:center}
/* footer */
.site-footer{top:4818px;left:0;width:1200px;height:307px;background:var(--blue);color:var(--white)}
.site-footer h5{font-size:15px;font-weight:500;letter-spacing:1px}
.foot-col{top:78px}
.foot-col .rule{height:3px;width:34px;margin:8px 0 18px}
.foot-col ul{list-style:none;font-size:14px;line-height:27px}
.foot-col ul li::before{content:"• ";color:var(--yellow)}
.foot-brand{left:446px;top:80px;width:360px;text-align:center}
.foot-brand .brand{justify-content:center;color:var(--white);font-size:30px}
.foot-brand .brand-dot{background:var(--white)}
.foot-brand p{font-size:14px;line-height:24px;margin-top:16px}
.socials{display:flex;justify-content:center;gap:10px;margin-top:12px}
.socials span{width:34px;height:34px;border-radius:50%;background:var(--yellow)}
.contact-line{display:flex;gap:16px;align-items:flex-start;font-size:13.5px;line-height:17px;margin-bottom:22px}
.contact-line .sq{flex:0 0 26px;height:26px;border:2px solid var(--white);border-radius:4px;display:flex;align-items:center;justify-content:center}
.bottom-bar{top:5125px;left:0;width:1200px;height:79px;background:var(--white);font-size:11px;color:var(--text)}
.badge{top:14px;width:60px;height:54px;border-radius:50%}
</style>
</head>
<body>

<header class="site-header abs">
  <div class="brand"><span class="brand-dot"></span>Velmora DX</div>
  <nav class="main-nav">
    <a class="active">Home</a><a>About Us</a><a>Products / Services</a><a>Blog</a><a class="pill">Contact Us</a>
  </nav>
</header>

<section class="hero abs">
  <div class="abs" style="inset:0" role="img" aria-label="Scientist in lab coat and goggles using a microscope beside monitors of research data"></div>
  <div class="hero-fade abs"></div>
  <div class="play abs"><svg width="52" height="52" viewBox="0 0 52 52"><path d="M21 17l14 9-14 9z" fill="#3a80d6"/></svg></div>
  <h1 class="abs">LIGHTING THE WAY TO EARLY<br>CANCER DETECTION</h1>
  <p class="abs">Highlight non-invasive, urine-based diagnostics</p>
  <a class="btn-yellow abs">CONTACT US</a>
</section>

<section class="features abs">
  <div class="feature"><div class="feature-icon y"><svg width="56" height="56" viewBox="0 0 56 56" fill="none" stroke="#fff" stroke-width="3"><circle cx="28" cy="28" r="24"/><path d="M11 45L45 11"/><rect x="22" y="14" width="10" height="24" rx="2"/><path d="M27 38v8M22 14h10"/></svg></div>Non-invasive<br>painless</div>
  <div class="feature"><div class="feature-icon b"><svg width="56" height="56" viewBox="0 0 56 56" fill="none" stroke="#fff" stroke-width="3"><circle cx="28" cy="28" r="22"/><circle cx="20" cy="22" r="4"/><circle cx="35" cy="20" r="3"/><circle cx="32" cy="35" r="5"/><circle cx="19" cy="36" r="2.5"/></svg></div>Precision<br>biomarkers</div>
  <div class="feature"><div class="feature-icon y"><svg width="56" height="56" viewBox="0 0 56 56" fill="none" stroke="#fff" stroke-width="3"><rect x="15" y="15" width="26" height="26" rx="3"/><path d="M22 8v7M28 8v7M34 8v7M22 41v7M28 41v7M34 41v7M8 22h7M8 28h7M8 34h7M41 22h7M41 28h7M41 34h7M22 34V26M28 34V22M34 34V29"/></svg></div>AI-powered<br>insights</div>
  <div class="feature"><div class="feature-icon b"><svg width="46" height="46" viewBox="0 0 46 46"><circle cx="23" cy="20" r="15" fill="none" stroke="#fff" stroke-width="3"/><path d="M16 20l5 5 9-10" fill="none" stroke="#fff" stroke-width="3"/><path d="M15 32l-4 11 7-3 4 5 3-9M31 32l4 11-7-3-4 5" fill="none" stroke="#fff" stroke-width="2.5"/></svg></div>Clinically validated &amp;<br>university spin-out<br>heritage</div>
</section>

<section class="about abs">
  <div class="about-photo-a abs" role="img" aria-label="Researcher in a mask working at a lab computer"></div>
  <div class="about-photo-b abs" role="img" aria-label="Microscopic view of a cell in blue and magenta light"></div>
  <div class="about-dot abs"></div>
  <h2 class="abs">About Us</h2>
  <div class="rule abs"></div>
  <h3 class="abs">Mission &amp; vision</h3>
  <p class="abs">Lorem ipsum dolor sit amet, consectetur adipiscing elit, sed do eiusmod tempor incididunt ut labore et dolore magna aliqua. Quis ipsum susp endisse ultrices gravida. Risus commodo viverra maecenas accumsan lacus vel facilisis. Lorem ipsum dolor sit amet, consectetur adipiscing elit, sed do eiusmod tempor incididunt ut labore et dolore magna aliqua. Quis ipsum suspendisse ultrices gravida. Risus commodo viv erra maec enas accumsan lacus vel facilisis.</p>
  <a class="btn-blue abs">KNOW MORE</a>
</section>

<section class="products abs" role="img" aria-label="Deep blue space background with a glowing planet edge">
  <h2 class="abs">Products / Services</h2>
  <div class="rule abs"></div>
  <div class="product-name abs">GlandSURE™</div>
  <div class="product-sub abs">(pancreatic cancer risk assessment &amp; surveillance).</div>
  <ul class="spec-list abs">
    <li><span class="spec-icon"><svg width="20" height="20" viewBox="0 0 20 20" fill="none" stroke="#fff" stroke-width="2"><circle cx="10" cy="7" r="3"/><path d="M4 17c0-4 3-6 6-6s6 2 6 6"/></svg></span><span><span class="k">Indication:</span> high-risk individuals (familial history, pancreatitis, genetic risk).</span></li>
    <li><span class="spec-icon"><svg width="20" height="20" viewBox="0 0 20 20" fill="none" stroke="#fff" stroke-width="2"><rect x="4" y="2" width="12" height="16" rx="1"/><path d="M7 7h6M7 10h6M7 13h4"/></svg></span><span><span class="k">Clinical output:</span> Elevated vs Average risk.</span></li>
    <li><span class="spec-icon"><svg width="20" height="20" viewBox="0 0 20 20" fill="none" stroke="#fff" stroke-width="2"><circle cx="10" cy="10" r="4"/><path d="M10 1v4M10 15v4M1 10h4M15 10h4"/></svg></span><span><span class="k">Development stage:</span> retrospective validation complete; prospective UroGland study in progress; UK launch Q4 2025.</span></li>
    <li><span class="spec-icon"><svg width="20" height="20" viewBox="0 0 20 20" fill="none" stroke="#fff" stroke-width="2"><circle cx="10" cy="10" r="8"/><circle cx="10" cy="10" r="4"/><circle cx="10" cy="10" r="1" fill="#fff"/></svg></span><span><span class="k">Target customers:</span> public health services, private hospitals, labs, pharma.</span></li>
  </ul>
  <div class="product-photo abs"><div role="img" aria-label="Clinicians reviewing scan results on a monitor"></div></div>
</section>

<div class="tile blue abs"><span class="t-icon"><svg width="50" height="50" viewBox="0 0 50 50" fill="none" stroke="#3a80d6" stroke-width="3.5"><circle cx="21" cy="21" r="13"/><path d="M31 31l12 12M21 15v12M15 21h12"/></svg></span><span>Future early<br>cancer<br>diagnostics</span></div>
<div class="tile sky abs"><span class="t-icon"><svg width="50" height="50" viewBox="0 0 50 50" fill="none" stroke="#7fd0f0" stroke-width="3.5"><path d="M16 5c0 10 18 10 18 20s-18 10-18 20M34 5c0 10-18 10-18 20s18 10 18 20M20 12h10M20 38h10M18 25h14"/></svg></span><span>Genetic<br>predisposition</span></div>
<div class="tile yellow abs"><span class="t-icon"><svg width="54" height="54" viewBox="0 0 54 54" fill="none" stroke="#f6c640" stroke-width="4"><path d="M7 38a20 20 0 0 1 40 0"/><path d="M27 38l10-14"/><circle cx="27" cy="38" r="3" fill="#f6c640"/></svg></span><span>Risk<br>scores.</span></div>

<article class="card abs" style="left:87px">
  <div class="img" role="img" aria-label="Scientist viewing glowing DNA helix displays" style="background:linear-gradient(135deg,#0c4a6e,#22b6d6 50%,#0a2a48)"></div>
  <h4>Technology</h4>
  <p>Approach: biomarker panels (urinary REG1B, LYVE1, TFF1; serum CA19-9; patient age).</p>
</article>
<article class="card abs" style="left:438px">
  <div class="img" role="img" aria-label="Lab technician handling samples beside a microscope" style="background:linear-gradient(135deg,#cfd6dc,#8a98a6 50%,#e9edf0)"></div>
  <h4>Science / Clinical Evidence</h4>
  <p>Published studies, peer-reviewed references.</p>
  <a class="btn-yellow">KNOW MORE</a>
</article>
<article class="card abs" style="left:788px">
  <div class="img" role="img" aria-label="Business partners shaking hands in an office" style="background:linear-gradient(135deg,#e6ebef,#6a86a6 55%,#c9d3dc)"></div>
  <h4>Partners &amp; Collaborations</h4>
  <p>Approach: biomarker panels (urinary REG1B, LYVE1, TFF1; serum CA19-9; patient age).</p>
</article>

<section class="blog">
  <h2 class="abs" style="top:3350px">Blog</h2>
  <div class="arrow abs" style="left:16px"><svg width="36" height="36"><path d="M20 12l-6 6 6 6" fill="none" stroke="#999" stroke-width="2"/></svg></div>
  <div class="arrow abs" style="left:1150px"><svg width="36" height="36"><path d="M16 12l6 6-6 6" fill="none" stroke="#333" stroke-width="2"/></svg></div>
  <article class="blog-card abs" style="left:73px">
    <div class="img" role="img" aria-label="Researcher at a microscope with screen data" style="background:linear-gradient(135deg,#e8ecef,#7b8fa4 60%,#c7d0d8)"></div>
    <div class="body"><div class="date">▪ MAY 20, 2025</div><h4>Lorem ipsum dolor sit amet. Sed pari aut accus</h4><p>Lorem ipsum dolor sit amet, con nsectetur adipiscing elit, sed do</p><span class="btn-blue">READ MORE</span></div>
  </article>
  <article class="blog-card abs" style="left:442px">
    <div class="img" role="img" aria-label="Doctor consulting with a patient" style="background:linear-gradient(135deg,#d9c7b4,#b7a28d 50%,#eef0f2)"></div>
    <div class="body"><div class="date">▪ MAY 20, 2025</div><h4>Lorem ipsum dolor sit amet. Sed pari aut accus</h4><p>Lorem ipsum dolor sit amet, con nsectetur adipiscing elit, sed do</p><span class="btn-blue">READ MORE</span></div>
  </article>
  <article class="blog-card abs" style="left:814px">
    <div class="img" role="img" aria-label="Petri dish and blue sample tubes" style="background:linear-gradient(135deg,#efe2b8,#f4f1ea 50%,#5ac0e0)"></div>
    <div class="body"><div class="date">▪ MAY 20, 2025</div><h4>Lorem ipsum dolor sit amet. Sed pari aut accus</h4><p>Lorem ipsum dolor sit amet, con nsectetur adipiscing elit, sed do</p><span class="btn-blue">READ MORE</span></div>
  </article>
</section>

<section class="contact">
  <h2 class="abs" style="top:4056px;left:80px">Contact Us</h2>
  <div class="rule abs"></div>
  <div class="contact-frame abs"><div role="img" aria-label="Scientist working at a microscope in front of monitors"></div></div>
  <div class="field abs" style="left:545px;top:4190px;width:265px;height:52px;padding-top:15px">First Name:</div>
  <div class="field abs" style="left:833px;top:4190px;width:264px;height:52px;padding-top:15px">Last Name:</div>
  <div class="field abs" style="left:545px;top:4267px;width:265px;height:52px;padding-top:15px">Phone:</div>
  <div class="field abs" style="left:833px;top:4267px;width:264px;height:52px;padding-top:15px">Email:</div>
  <div class="field abs" style="left:545px;top:4344px;width:552px;height:170px">Message:</div>
  <a class="btn-blue abs">ONBOARD YOUR CLINIC</a>
  <div class="info abs" style="left:128px"><span class="ic" style="background:var(--blue)"><svg width="24" height="24" viewBox="0 0 24 24" fill="none" stroke="#fff" stroke-width="2"><rect x="3" y="6" width="18" height="13" rx="1"/><path d="M3 7l9 7 9-7"/></svg></span><span>EMAIL US<br>info@websitename.com</span></div>
  <div class="info abs" style="left:458px"><span class="ic" style="background:var(--sky)"><svg width="24" height="24" viewBox="0 0 24 24" fill="none" stroke="#fff" stroke-width="2.2"><path d="M10 14a4 4 0 0 0 6 0l3-3a4 4 0 0 0-6-6l-1 1M14 10a4 4 0 0 0-6 0l-3 3a4 4 0 0 0 6 6l1-1"/></svg></span><span>LINKEDIN<br>@websitename.com</span></div>
  <div class="info abs" style="left:762px"><span class="ic" style="background:var(--yellow)"><svg width="24" height="24" viewBox="0 0 24 24" fill="none" stroke="#fff" stroke-width="2.2"><path d="M12 22s7-7 7-12a7 7 0 0 0-14 0c0 5 7 12 7 12z"/><circle cx="12" cy="10" r="2.5"/></svg></span><span>Address line Dummy Here<br>Address line Here</span></div>
</section>

<footer class="site-footer abs">
  <div class="foot-col abs" style="left:233px">
    <h5>QUICK LINKS</h5><div class="rule"></div>
    <ul><li>Home</li><li>About Us</li><li>Products/Services</li><li>Blog</li><li>Contact Us</li></ul>
  </div>
  <div class="foot-brand abs">
    <div class="brand"><span class="brand-dot"></span>Velmora DX</div>
    <p>Lorem ipsum dolor sit amet, consectetur<br>adipiscing elit, sed do eiusmod tempor</p>
    <div class="socials"><span></span><span></span><span></span></div>
  </div>
  <div class="foot-col abs" style="left:858px">
    <h5>CONTACT US</h5><div class="rule"></div>
    <div class="contact-line"><span class="sq"><svg width="14" height="14" viewBox="0 0 14 14" fill="none" stroke="#fff" stroke-width="1.6"><path d="M3 1l2 3-1 1.5c1 2 2.5 3.5 4.5 4.5L10 9l3 2-1 2C7 13 1 7 1 2z"/></svg></span><span>CALL US<br>8012 345 6789</span></div>
    <div class="contact-line"><span class="sq"><svg width="14" height="14" viewBox="0 0 14 14" fill="none" stroke="#fff" stroke-width="1.6"><rect x="1" y="3" width="12" height="8"/><path d="M1 3l6 5 6-5"/></svg></span><span>EMAIL US<br>info@websitename.com</span></div>
    <div class="contact-line"><span class="sq"><svg width="14" height="14" viewBox="0 0 14 14" fill="none" stroke="#fff" stroke-width="1.6"><path d="M7 13s4-4 4-7a4 4 0 0 0-8 0c0 3 4 7 4 7z"/><circle cx="7" cy="6" r="1.3"/></svg></span><span>Address line Dummy Here<br>Address line Here</span></div>
  </div>
</footer>

<div class="bottom-bar abs">
  <span class="abs" style="left:75px;top:32px">Copyright © 2025 All Rights Reserved By Company name</span>
  <span class="abs" style="left:428px;top:32px">Privacy Policy, Terms of Use, GDPR, Accessibility</span>
  <span class="badge abs" style="left:838px;background:#2b2b33;border-radius:28px;width:100px;height:44px;top:18px"></span>
  <span class="badge abs" style="left:960px;background:var(--sky)"></span>
  <span class="badge abs" style="left:1062px;background:#8a2b6a;border-radius:8px;width:54px"></span>
</div>

</body>
</html>
```